I need a book cover for my book titled Sunny Porch! The subtitle is Quiet Orchard Days and the the author is Marisol Dunleavy. I want the attached photo included on the cover, plus the words "I never met a chicken wing I didn't like!" The book size is 5.06 x 7.81 in. and is 146 pages. For the color scheme, I like a chocolate brown cover with aqua blue letters. (Please note that you don't have to use these colors. Feel free to use this color scheme or whatever you colors you like!)

• Please include my photo for the back cover, along with this text:

Sunny Porch! I was tired of being tired! I was tired of acid reflux, body stiffness, and being overweight. To make matters worse, I suffered from back pain, constipation, leg pain, and lack of sleep. If you are tired of looking to medical test for your answers, this is the book for you. The key was the day I decided to make “me” a priority by being #1 on my “to-do” list.

Our healthcare system seems to be more concerned about treating illness than they are about preventing it; which is why we have so many problems with our health and wellness. That’s why I’m going to give you insights into nutrition, health care, and the pharmaceutical industry.

I’m also going to give you some insights into exercise, supplements, detoxing and essential oils; as well as what goes into your grocery cart and the foods you feed your family.

Because you’re reading this I know you’re ready to live your best life, Sunny Porch! is for you.

Here’s to a healthy you!

Here's a brief bio about the author for the back cover:

Marisol lives in Chicago with her husband, Dr. Wendell, and has three adult children. She is probably one of the most private people you will meet – BUT HAD to tell her story!

```html
<!DOCTYPE html>
<html lang="en">
<head>
<meta charset="utf-8">
<title>Sunny Porch! – Quiet Orchard Days – Cover Spread</title>
<link href="https://fonts.googleapis.com/css2?family=Great+Vibes&family=Cinzel:wght@400&family=Source+Sans+3:wght@400&family=Tinos&display=swap" rel="stylesheet">
<style>
  :root {
    --brown-top: #c0905a;
    --brown-mid: #5b3a1f;
    --brown-deep: #1e120a;
    --ink-black: #050302;
    --aqua: #6cb9ea;
    --aqua-body: #86c8ee;
    --aqua-band: #38a6e6;
    --gold: #e3a21f;
    --white: #ffffff;
    --dish-light: #ece7e0;
    --dish-sauce: #b4512c;
    --dish-deep: #7a3519;
  }
  * { margin: 0; padding: 0; box-sizing: border-box; }
  html, body { width: 1200px; height: 894px; overflow: hidden; background: var(--ink-black); }
  .cover-spread {
    position: relative;
    width: 1200px;
    height: 894px;
    background: linear-gradient(to bottom, var(--brown-top) 0%, #9a6a3c 22%, var(--brown-mid) 48%, var(--brown-deep) 75%, var(--ink-black) 100%);
    overflow: hidden;
  }
  .script { font-family: "Great Vibes", cursive; color: var(--aqua); font-weight: 400; }

  /* Back cover */
  .back-heading { position: absolute; left: 62px; top: 56px; font-size: 56px; line-height: 1; white-space: nowrap; }
  .back-copy {
    position: absolute; left: 64px; top: 128px; width: 455px;
    font-family: "Source Sans 3", sans-serif; font-size: 15.4px; line-height: 17.5px;
    color: var(--aqua-body); text-align: center;
  }
  .back-copy p { margin-bottom: 17.5px; }
  .back-signoff { position: absolute; left: 64px; top: 468px; width: 455px; text-align: center; font-size: 28px; line-height: 1; }
  .bio-band {
    position: absolute; left: 64px; top: 551px; width: 455px; height: 142px;
    background: var(--aqua-band);
  }
  .bio-text {
    position: absolute; left: 194px; top: 564px; width: 316px;
    font-family: "Tinos", serif; font-size: 15.5px; line-height: 22.3px;
    color: var(--white); text-align: center; white-space: nowrap;
  }
  .author-photo {
    position: absolute; left: 75px; top: 518px; width: 117px; height: 207px;
    border: 1px solid #c8a060;
    background: linear-gradient(160deg, #6a4a2a, #3a2414 55%, #8a6a40);
  }

  /* Spine */
  .spine-title, .spine-subtitle, .spine-author {
    position: absolute; writing-mode: vertical-rl; white-space: nowrap; line-height: 1;
  }
  .spine-title { left: 582px; top: 84px; font-size: 38px; }
  .spine-subtitle { left: 588px; top: 268px; font-family: "Cinzel", serif; font-size: 27px; color: var(--gold); letter-spacing: 1px; }
  .spine-author { left: 590px; top: 598px; font-family: "Tinos", serif; font-size: 23px; color: var(--aqua); letter-spacing: 1.5px; }

  /* Front cover */
  .front-title { position: absolute; left: 660px; top: 96px; width: 500px; text-align: center; font-size: 86px; line-height: 1; white-space: nowrap; }
  .front-subtitle {
    position: absolute; left: 630px; top: 224px; width: 560px; text-align: center;
    font-family: "Cinzel", serif; font-size: 38px; line-height: 1; color: var(--gold); letter-spacing: 1px;
  }
  .front-photo {
    position: absolute; left: 698px; top: 378px; width: 422px; height: 290px;
    border-radius: 18px;
    background: linear-gradient(150deg, var(--dish-light) 0%, #d9b9a2 35%, var(--dish-sauce) 65%, var(--dish-deep) 100%);
  }
  .front-quote {
    position: absolute; left: 620px; top: 732px; width: 580px; text-align: center;
    font-family: "Tinos", serif; font-size: 22px; line-height: 1; color: var(--aqua); letter-spacing: 0.3px; white-space: nowrap;
  }
  .front-author {
    position: absolute; left: 630px; top: 776px; width: 560px; text-align: center;
    font-family: "Cinzel", serif; font-size: 38px; line-height: 1; color: var(--gold); letter-spacing: 1px;
  }
</style>
</head>
<body>
<main class="cover-spread">
  <section class="back-cover">
    <h2 class="script back-heading">Sunny Porch!</h2>
    <div class="back-copy">
      <p>I was tired of being tired! I was tired of acid reflux, body stiffness, and being overweight. To make matters worse, I suffered from back pain, constipation, leg pain, and lack of sleep. If you are tired of looking to medical test for your answers, this is the book for you. The key was the day I decided to make “me” a priority by being #1 on my “to-do” list.</p>
      <p>Our healthcare system seems to be more concerned about treating illness than they are about preventing it; which is why we have so many problems with our health and wellness. That’s why I’m going to give you insights into nutrition, health care, and the pharmaceutical industry.</p>
      <p>I’m also going to give you some insights into exercise, supplements, detoxing and essential oils; as well as what goes into your grocery cart and the foods you feed your family.</p>
      <p>Because you’re reading this I know you’re ready to live your best life, Sunny Porch! is for you.</p>
    </div>
    <p class="script back-signoff">Here’s to a healthy you!</p>
    <div class="bio-band"></div>
    <div class="author-photo" role="img" aria-label="Portrait photo of the author"></div>
    <p class="bio-text">Marisol lives in Chicago with her husband,<br>Dr. Wendell, and has three adult children.<br>She is probably one of the most private<br>people you will meet –<br>BUT HAD to tell her story!</p>
  </section>

  <section class="spine">
    <span class="script spine-title">Sunny Porch!</span>
    <span class="spine-subtitle">QUIET ORCHARD DAYS</span>
    <span class="spine-author">MARISOL DUNLEAVY</span>
  </section>

  <section class="front-cover">
    <h1 class="script front-title">Sunny Porch!</h1>
    <p class="front-subtitle">QUIET ORCHARD DAYS</p>
    <div class="front-photo" role="img" aria-label="Photo of glazed chicken wings with celery, carrots and dip in a white dish marked with warning labels"></div>
    <p class="front-quote">"I NEVER MET A CHICKEN WING I DIDN'T LIKE!"</p>
    <p class="front-author">MARISOL DUNLEAVY</p>
  </section>
</main>
</body>
</html>
```